Newsletter Ad

I am looking for someone to design an advertisement for a mother's club newsletter. 4" wide X by 5" tall (and 2.5" wide X 5" tall if possible).

I'm a psychotherapist, so want the ad to look professional, but modern. I have a logo with my photo attached that can be incorporated into the design. The colors of my website are turquoise and white. I'd like to keep with that theme...so maybe some turquoise blocking to match the logo font color.

I'm uploading a logo as well as an ad draft with the content I'd like listed in the ad.

```html
<!DOCTYPE html>
<html lang="en">
<head>
<meta charset="UTF-8">
<title>Dana Morel, MA, MFT — Psychotherapy</title>
<link rel="stylesheet" href="https://fonts.googleapis.com/css2?family=Questrial&display=swap">
<style>
  :root {
    --turquoise: #22bfb5;
    --ink: #111111;
    --rule: #1a1a1a;
    --panel: #e4e2de;
    --paper: #ffffff;
    --portrait-light: #c9a88a;
    --portrait-dark: #5a3f2e;
  }
  * { margin: 0; padding: 0; box-sizing: border-box; }
  html, body { width: 961px; height: 1200px; overflow: hidden; background: var(--paper); }
  .ad {
    position: relative;
    width: 961px;
    height: 1200px;
    background: var(--paper);
    font-family: "Questrial", "Century Gothic", sans-serif;
    color: var(--ink);
  }
  .portrait {
    position: absolute;
    left: 0; top: 0;
    width: 234px; height: 363px;
    background: linear-gradient(160deg, var(--portrait-light) 0%, #9c7558 45%, var(--portrait-dark) 100%);
  }
  .practitioner-name {
    position: absolute;
    left: 236px; top: 96px;
    width: 574px;
    font-size: 63px;
    font-weight: 400;
    line-height: 1;
    letter-spacing: 0.5px;
    color: var(--turquoise);
    white-space: nowrap;
  }
  .name-rule {
    position: absolute;
    left: 207px; top: 175px;
    width: 599px; height: 3px;
    background: var(--rule);
  }
  .service-title {
    position: absolute;
    left: 207px; top: 198px;
    width: 599px;
    text-align: center;
    line-height: 1;
  }
  .service-title .main { font-size: 58px; }
  .service-title .for { font-size: 32px; margin-left: 6px; }
  .service-audience {
    position: absolute;
    left: 207px; top: 272px;
    width: 599px;
    text-align: center;
    font-size: 33px;
    line-height: 1;
    white-space: nowrap;
  }
  .specialties {
    position: absolute;
    left: 0; top: 363px;
    width: 961px;
    list-style: none;
  }
  .specialties li {
    height: 54px;
    margin-bottom: 7px;
    background: var(--panel);
    font-size: 40px;
    line-height: 54px;
    text-align: center;
  }
  .specialties li:first-child { height: 118px; padding-top: 64px; }
  .specialties li:last-child { height: 80px; margin-bottom: 0; padding-bottom: 26px; }
  .contact-band {
    position: absolute;
    left: 0; top: 945px;
    width: 961px; height: 176px;
    background: var(--turquoise);
    color: var(--paper);
    text-align: center;
    padding-top: 24px;
  }
  .contact-band .address { font-size: 34px; line-height: 36px; }
  .contact-band .detail { font-size: 28px; line-height: 33px; }
  .license {
    position: absolute;
    right: 29px; top: 1138px;
    font-size: 23px;
    line-height: 1;
  }
</style>
</head>
<body>
  <div class="ad">
    <div class="portrait" role="img" aria-label="Portrait photograph of the therapist"></div>

    <h1 class="practitioner-name">DANA MOREL, MA, MFT</h1>
    <div class="name-rule"></div>

    <p class="service-title"><span class="main">Psychotherapy</span><span class="for">for</span></p>
    <p class="service-audience">Individuals, Couples and Families</p>

    <ul class="specialties">
      <li>Parenting</li>
      <li>Depression</li>
      <li>Anxiety</li>
      <li>Life Transitions</li>
      <li>Divorce</li>
      <li>Couples Issues</li>
      <li>Women’s Issues</li>
      <li>Attachment and Neuroscience</li>
    </ul>

    <address class="contact-band" style="font-style: normal;">
      <p class="address">418 Cedar Lane, Alder Bay, CA 94960</p>
      <p class="detail">www.danamorel.com</p>
      <p class="detail">dana@danamorel.com</p>
      <p class="detail">415.555.0148</p>
    </address>

    <p class="license">License# MFC48210</p>
  </div>
</body>
</html>
```